Business Card Design

I am an child sleep consultant. I would like the picture to be the background of the card and for my logo to be in the upper right hand corner. Other than that, the design is yours!!

Business

Marta Kovel
Red Fern Slumber
Certified Child Sleep Consultant
(555) 286-9153
redfernslumber.com

```html
<!DOCTYPE html>
<html lang="en">
<head>
<meta charset="utf-8">
<title>Red Fern Slumber – Business Card</title>
<link href="https://fonts.googleapis.com/css2?family=Michroma&family=Hind:wght@400;500&display=swap" rel="stylesheet">
<style>
  :root {
    --stage: #5f5f5f;
    --photo-base: #cfc7c5;
    --photo-skin: #ece4e1;
    --photo-skin-shade: #c9bdb9;
    --photo-back-light: #ded8d6;
    --photo-back-mid: #a9a09e;
    --photo-ground: #5e5755;
    --photo-cloth: #8f8683;
    --band-pink: #f4abc8;
    --band-fade: rgba(244, 171, 200, 0);
    --edge-pink: #e8658c;
    --name-rose: #df4a6a;
    --ink: #3d3a3d;
    --icon-bg: #2f2f33;
    --white: #ffffff;
  }
  html, body {
    margin: 0;
    width: 1200px;
    height: 1000px;
    overflow: hidden;
    background: var(--stage);
  }
  .card {
    position: absolute;
    left: 100px;
    top: 207px;
    width: 1000px;
    height: 585px;
    overflow: hidden;
    background: var(--photo-base);
    box-shadow: 0 6px 18px rgba(0,0,0,.35);
  }
  .card__photo {
    position: absolute;
    inset: 0;
    background:
      radial-gradient(ellipse 24% 46% at 35% 38%, var(--photo-skin) 0%, var(--photo-skin) 55%, var(--photo-skin-shade) 80%, rgba(201,189,185,0) 100%),
      radial-gradient(ellipse 32% 22% at 34% 90%, var(--photo-cloth) 0%, rgba(143,134,131,0) 100%),
      linear-gradient(180deg,
        var(--photo-back-light) 0%,
        #d2cbc9 30%,
        var(--photo-back-mid) 48%,
        var(--photo-ground) 58%,
        #7a716f 68%,
        #b4abaa 80%,
        #c9c1bf 100%),
      var(--photo-base);
  }
  .card__glow {
    position: absolute;
    left: 690px;
    top: 10px;
    width: 330px;
    height: 330px;
    border-radius: 50%;
    background: radial-gradient(circle, var(--white) 0%, var(--white) 48%, rgba(255,255,255,.85) 58%, rgba(255,255,255,0) 72%);
  }
  .brand {
    position: absolute;
    left: 770px;
    top: 108px;
    width: 170px;
    text-align: center;
    font-family: "Hind", sans-serif;
    font-weight: 500;
    font-size: 26px;
    line-height: 1.1;
    color: var(--ink);
  }
  .brand__dot {
    display: block;
    width: 46px;
    height: 46px;
    margin: 0 auto 10px;
    border-radius: 50%;
    background: var(--band-pink);
  }
  .card__band {
    position: absolute;
    left: 0;
    right: 0;
    top: 380px;
    height: 195px;
    background: linear-gradient(180deg, var(--band-fade) 0%, var(--band-pink) 24%, var(--band-pink) 100%);
  }
  .card__edge {
    position: absolute;
    left: 0;
    right: 0;
    bottom: 0;
    height: 10px;
    background: var(--edge-pink);
  }
  .identity {
    position: absolute;
    left: 60px;
    top: 432px;
    width: 370px;
    text-align: center;
  }
  .identity__name {
    margin: 0;
    font-family: "Michroma", sans-serif;
    font-size: 36px;
    line-height: 50px;
    font-weight: 400;
    color: var(--name-rose);
    letter-spacing: 1px;
    white-space: nowrap;
  }
  .identity__role {
    margin: 2px 0 0;
    font-family: "Hind", sans-serif;
    font-size: 26px;
    line-height: 1.1;
    color: var(--ink);
  }
  .contacts {
    position: absolute;
    left: 455px;
    top: 442px;
    margin: 0;
    padding: 0;
    list-style: none;
    font-family: "Hind", sans-serif;
    font-size: 26px;
    color: var(--ink);
  }
  .contacts__item {
    display: flex;
    align-items: center;
    gap: 14px;
    height: 38px;
  }
  .contacts__icon {
    width: 22px;
    height: 22px;
    flex: none;
  }
</style>
</head>
<body>
  <div class="card">
    <div class="card__photo" role="img" aria-label="Soft black-and-white photograph of a smiling baby filling the card background"></div>
    <div class="card__glow"></div>

    <div class="brand">
      <span class="brand__dot"></span>
      Red Fern Slumber
    </div>

    <div class="card__band"></div>
    <div class="card__edge"></div>

    <div class="identity">
      <h1 class="identity__name">Marta Kovel</h1>
      <p class="identity__role">Red Fern Slumber Certified<br>Child Sleep Consultant</p>
    </div>

    <ul class="contacts">
      <li class="contacts__item">
        <svg class="contacts__icon" viewBox="0 0 22 22" aria-hidden="true">
          <rect width="22" height="22" rx="4" fill="var(--icon-bg)"/>
          <path d="M8 5 L10 5 L10.5 8 L9 9 Q10 12 13 13.5 L14 12 L17 12.5 L17 14.5 Q16.5 17 14 17 Q6 15 5 8 Q5 5 8 5 Z" fill="var(--white)"/>
        </svg>
        <span>(555) 286-9153</span>
      </li>
      <li class="contacts__item">
        <svg class="contacts__icon" viewBox="0 0 22 22" aria-hidden="true">
          <rect width="22" height="22" rx="4" fill="var(--icon-bg)"/>
          <rect x="5" y="7" width="12" height="9" rx="1" fill="var(--white)"/>
          <path d="M5 7.5 L11 12 L17 7.5" stroke="var(--icon-bg)" stroke-width="1.3" fill="none"/>
        </svg>
        <span>hello@slumbermail.com</span>
      </li>
      <li class="contacts__item">
        <svg class="contacts__icon" viewBox="0 0 22 22" aria-hidden="true">
          <rect width="22" height="22" rx="4" fill="var(--icon-bg)"/>
          <circle cx="11" cy="11" r="6" fill="none" stroke="var(--white)" stroke-width="1.4"/>
          <ellipse cx="11" cy="11" rx="2.6" ry="6" fill="none" stroke="var(--white)" stroke-width="1.2"/>
          <line x1="5" y1="11" x2="17" y2="11" stroke="var(--white)" stroke-width="1.2"/>
        </svg>
        <span>redfernslumber.com</span>
      </li>
    </ul>
  </div>
</body>
</html>
```